New Zealand Export company needs business cards

We need new business cards to match our new logo for a company based in New Zealand who deal specifically with the Pacific Islands. We source, consolidate and ship products out of New Zealand to the Pacific Islands. Will attach our old ones and also new logo.
Would like the Islands we deal with and the areas of work we have access to, to be included on the business cards.

Contact Information for Business Card

T +64 9 571 3048
F +64 9 571 6285
12-18 Kowhai Lane, Drury, 2113
PO Box 814, Drury, Auckland 2247, New Zealand
www.falconfreight.example.nz
E sales@falconfreight.example.nz

Font styles to use
Sans Serif

Colors
85abd2
33a6d7
ffffff

Requirements
Must have
• A company of PWM

```html
<!DOCTYPE html>
<html lang="en">
<head>
<meta charset="utf-8">
<title>Falcon Freight — Business Card</title>
<link href="https://fonts.googleapis.com/css2?family=Lato:wght@400;700;900&display=swap" rel="stylesheet">
<style>
  :root {
    --navy: #0d57a3;
    --sky: #33a6d7;
    --ink: #2a2d6b;
    --paper: #ffffff;
    --paper-shade: #f1f2f3;
    --stage: #e4e6e8;
    --edge: #0d57a3;
  }
  * { box-sizing: border-box; margin: 0; padding: 0; }
  html, body {
    width: 1200px; height: 900px; overflow: hidden;
    background: var(--stage);
    font-family: "Lato", sans-serif;
  }
  .stage {
    width: 1200px; height: 900px;
    display: flex; flex-direction: column;
    align-items: center; justify-content: center; gap: 36px;
  }
  .card {
    position: relative;
    width: 700px; height: 400px;
    background: linear-gradient(135deg, var(--paper) 0%, var(--paper-shade) 100%);
    border-bottom: 6px solid var(--edge);
    box-shadow: 0 10px 24px rgba(0,0,0,0.18);
  }

  /* brand lockup */
  .brand { display: flex; align-items: center; gap: 14px; }
  .brand-square { width: 38px; height: 38px; background: var(--navy); }
  .brand-name {
    font-weight: 900; color: var(--navy);
    font-size: 40px; letter-spacing: 1px; text-transform: uppercase;
  }

  /* front */
  .card-front .brand { position: absolute; left: 56px; top: 174px; }
  .card-front .brand-square { width: 30px; height: 30px; }
  .card-front .brand-name { font-size: 30px; }
  .contact {
    position: absolute; left: 392px; top: 62px;
    color: var(--sky); font-size: 15px; line-height: 1.35;
  }
  .contact-name { color: var(--navy); font-weight: 900; font-size: 27px; line-height: 1.1; }
  .contact-role { font-size: 16px; margin-bottom: 14px; }
  .contact-address { margin-bottom: 16px; }
  .contact-lines { list-style: none; }
  .contact-lines li { display: flex; align-items: center; gap: 10px; height: 22px; }
  .contact-lines svg { width: 16px; height: 16px; fill: var(--navy); flex: none; }

  /* back */
  .card-back .brand { position: absolute; left: 0; right: 0; top: 168px; justify-content: center; }
  .card-back .brand-square { width: 48px; height: 48px; }
  .card-back .brand-name { font-size: 54px; }
  .parent {
    position: absolute; right: 40px; bottom: 34px;
    display: flex; align-items: center; gap: 10px;
    color: var(--ink); font-size: 15px;
  }
  .parent-name { font-weight: 900; font-size: 20px; letter-spacing: 1px; }
</style>
</head>
<body>
<main class="stage">

  <section class="card card-front">
    <div class="brand">
      <span class="brand-square"></span>
      <span class="brand-name">Falcon Freight</span>
    </div>

    <div class="contact">
      <p class="contact-name">Tessa Langford</p>
      <p class="contact-role">Sales Manager</p>
      <p class="contact-address">12-18 Kowhai Lane, Drury, 2113<br>PO Box 814, Drury,<br>Auckland 2247, New Zealand</p>
      <ul class="contact-lines">
        <li>
          <svg viewBox="0 0 16 16" aria-hidden="true"><path d="M1 5c0-2 3-3 7-3s7 1 7 3v1.5h-3.5V5h-7v1.5H1zM3.5 8l1.5-1.5h6L12.5 8 14 14H2z"/></svg>
          +64 9 571 3048
        </li>
        <li>
          <svg viewBox="0 0 16 16" aria-hidden="true"><path d="M4 1h8v4H4zM1 6h14v6h-3v3H4v-3H1zm4 5v3h6v-3z"/></svg>
          +64 9 571 6285
        </li>
        <li>
          <svg viewBox="0 0 16 16" aria-hidden="true"><path d="M1 3h14v10H1zm1.5 1.5L8 9l5.5-4.5z"/></svg>
          sales@falconfreight.example.nz
        </li>
        <li>
          <svg viewBox="0 0 16 16" aria-hidden="true"><circle cx="8" cy="8" r="7" fill="none" stroke="currentColor" style="stroke:var(--navy)" stroke-width="1.4"/><path d="M1 8h14M8 1v14" stroke="var(--navy)" stroke-width="1.2"/><ellipse cx="8" cy="8" rx="3" ry="7" fill="none" stroke="var(--navy)" stroke-width="1.2"/></svg>
          www.falconfreight.example.nz
        </li>
      </ul>
    </div>
  </section>

  <section class="card card-back">
    <div class="brand">
      <span class="brand-square"></span>
      <span class="brand-name">Falcon Freight</span>
    </div>
    <div class="parent">
      <span>A company of</span>
      <span class="parent-name">PWM</span>
    </div>
  </section>

</main>
</body>
</html>
```